Web Calculator design Housing Investment

We have a web calculator that needs to be fixed from a design perspective. The key tasks are:<br/>1. Selecting icons / pictures / colours for the various steps<br/>2. Designing navigation between calculator steps<br/>3. Making suggestions for chart design. The limitation is that the charts are all using the Tarvo API (the same charts that Tarvo Grids use).<br/><br/>There are four entry screens and then a result screen. See attached PDF for screenshots. You can see our website at https://brindlecapital.com for our corporate colours and style.

Target Market(s)

Real Estate Investors

Industry/Entity Type

Financial Planning

Number of Pages Required

1 page

Font styles to use
Sans Serif
Other font styles liked:
• Ubuntu

Colors
86cae7
3176b5
0455a3
ffffff

Requirements
Must have
• New Icons
• Suggested design for navigation
• Suggested design for charts

```html
<!DOCTYPE html>
<html lang="en">
<head>
<meta charset="utf-8">
<title>Halvard Wealth — Property Calculator Screens</title>
<link href="https://fonts.googleapis.com/css2?family=Ubuntu:wght@300;400;500;700&display=swap" rel="stylesheet">
<style>
  :root{
    --sky:#86cae7;
    --mid:#3176b5;
    --navy:#0455a3;
    --white:#ffffff;
    --page:#eef1f5;
    --ink:#1f2a37;
    --muted:#8a94a3;
    --line:#d5dbe3;
    --footer:#2d2f33;
    --dark-panel:#1c2330;
    --dark-cell:#252e3d;
  }
  *{box-sizing:border-box;margin:0;padding:0}
  html,body{width:1200px;height:3196px;overflow:hidden}
  body{background:var(--page);font-family:"Ubuntu",sans-serif;color:var(--ink);position:relative}

  .screen{position:absolute;left:32px;width:1136px;background:var(--white);box-shadow:0 2px 10px rgba(4,85,163,.08)}
  .screen--type{top:8px;height:592px}
  .screen--location{top:660px;height:580px}
  .screen--valuation{top:1300px;height:568px}
  .screen--forecast{top:1940px;height:572px}
  .screen--calc{top:2580px;height:544px}

  .stepper{position:absolute;left:0;top:0;width:880px;height:90px}
  .stepper__track{position:absolute;left:84px;top:44px;width:692px;height:2px;background:var(--line)}
  .stepper__progress{position:absolute;left:84px;top:44px;height:2px;background:var(--navy)}
  .step{position:absolute;top:14px;width:120px;margin-left:-60px;text-align:center}
  .step__num{font-size:13px;color:var(--muted);display:block;height:18px}
  .step__dot{width:14px;height:14px;border-radius:50%;border:2px solid var(--line);background:var(--white);margin:4px auto 6px}
  .step__label{font-size:11px;color:var(--muted);white-space:nowrap}
  .step--done .step__dot{border-color:var(--navy)}
  .step--done .step__num{color:var(--navy)}
  .step--active .step__dot{background:var(--navy);border-color:var(--navy)}
  .step--active .step__num,.step--active .step__label{color:var(--navy);font-weight:500}
  .step--done .step__dot svg{display:block;margin:0}

  .nav{position:absolute;right:32px;top:24px;display:flex;gap:10px}
  .btn{height:34px;padding:0 20px;border-radius:17px;font:500 14px "Ubuntu",sans-serif;display:flex;align-items:center}
  .btn--primary{background:var(--navy);color:var(--white)}
  .btn--ghost{border:2px solid var(--navy);color:var(--navy);background:var(--white)}

  .title{position:absolute;left:0;width:100%;text-align:center;font-weight:400;font-size:30px;line-height:38px;color:var(--ink)}
  .footer{position:absolute;left:0;bottom:0;width:100%;height:30px;background:var(--footer);color:#b9bec6;font-size:11px;display:flex;align-items:center;justify-content:center}

  .type-tiles{position:absolute;top:196px;left:452px;display:flex;gap:16px}
  .tile{width:108px;height:128px;background:var(--navy);border:3px solid var(--navy);display:flex;flex-direction:column}
  .tile--selected{outline:3px solid var(--sky)}
  .tile__art{flex:1;background:linear-gradient(160deg,#3a86c8,#0c3f7a)}
  .tile__art--house{background:linear-gradient(160deg,#5f89b8,#12355e)}
  .tile__label{height:26px;color:var(--white);font-size:14px;display:flex;align-items:center;justify-content:center}

  .map{position:absolute;left:150px;top:150px;width:190px;height:170px;background:linear-gradient(150deg,#3a9ae6,#0455a3)}
  .slider-group{position:absolute;left:540px;width:420px}
  .slider-group__label{font-size:12px;color:#556070;display:flex;align-items:center;gap:6px}
  .slider{position:relative;height:18px;margin-top:8px}
  .slider__rail{position:absolute;left:0;right:0;top:7px;height:4px;border-radius:2px;background:var(--line)}
  .slider__fill{position:absolute;left:0;top:7px;height:4px;border-radius:2px;background:var(--navy)}
  .slider__knob{position:absolute;top:1px;width:16px;height:16px;border-radius:50%;background:var(--navy);border:3px solid var(--white);box-shadow:0 0 0 1px var(--navy)}
  .slider-group__value{position:absolute;right:-90px;top:22px;font-size:12px;color:#556070}
  .info{width:13px;height:13px;border-radius:50%;border:1px solid var(--muted);font-size:9px;color:var(--muted);display:inline-flex;align-items:center;justify-content:center}

  .methods{position:absolute;top:200px;left:0;width:100%;display:flex;justify-content:center;gap:100px}
  .method{width:200px;text-align:center}
  .method__icon{width:88px;height:88px;margin:0 auto;position:relative}
  .method__diamond{position:absolute;inset:12px;transform:rotate(45deg);border:2px solid var(--line);background:var(--white)}
  .method__art{position:absolute;left:26px;top:26px;width:36px;height:36px;border-radius:4px}
  .method__name{margin-top:18px;font-size:17px;font-weight:500;color:var(--ink)}
  .method__desc{margin-top:8px;font-size:10px;line-height:14px;color:var(--muted)}

  .forecast-title{top:100px;font-weight:500;font-size:28px}
  .field{position:absolute;left:150px;width:620px;display:flex;align-items:center;justify-content:flex-end;gap:8px;font-size:12px;color:#556070}
  .field__input{width:168px;height:28px;border:1px solid var(--line);font-size:11px;color:var(--muted);display:flex;align-items:center;padding-left:8px}
  .field__btn{width:24px;height:28px;background:var(--navy);display:flex;align-items:center;justify-content:center}
  .chart{position:absolute;left:88px;top:226px}
  .forecast-note{position:absolute;left:100px;top:402px;font-size:11px;color:#556070}
  .forecast-slider{position:absolute;left:100px;top:422px;width:340px}

  .results{position:absolute;left:20px;top:110px;width:1096px;height:196px;background:var(--dark-panel);display:flex;gap:6px;padding:8px}
  .results__cell{background:var(--dark-cell);flex:1;position:relative}
  .results__cell--inputs{flex:0 0 300px;padding:14px 14px}
  .kv{display:flex;justify-content:space-between;align-items:center;font-size:10px;color:#a9b3c2;height:22px;margin-bottom:10px}
  .kv__box{width:118px;height:18px;background:#1a212c;border:1px solid #3b475a;color:#d9e2ee;font-size:10px;padding-left:6px;display:flex;align-items:center}
  .tooltip{position:absolute;right:10px;top:10px;width:120px;background:#0f1520;border:1px solid #3b475a;padding:8px;font-size:10px;line-height:15px;color:#d9e2ee}
  .tooltip b{color:var(--sky);font-weight:500}
  .results-note{position:absolute;left:140px;top:322px;width:856px;text-align:center;font-size:11px;line-height:16px;color:var(--muted)}
</style>
</head>
<body>

<section class="screen screen--type">
  <div class="stepper">
    <div class="stepper__track"></div>
    <div class="step step--active" style="left:116px"><span class="step__num">01</span><div class="step__dot"></div><span class="step__label">Property Type</span></div>
    <div class="step" style="left:289px"><span class="step__num">02</span><div class="step__dot"></div><span class="step__label">Property Location</span></div>
    <div class="step" style="left:462px"><span class="step__num">03</span><div class="step__dot"></div><span class="step__label">Property Valuation</span></div>
    <div class="step" style="left:635px"><span class="step__num">04</span><div class="step__dot"></div><span class="step__label">Your Property Forecast</span></div>
    <div class="step" style="left:808px"><span class="step__num">05</span><div class="step__dot"></div><span class="step__label">Calculation</span></div>
  </div>
  <div class="nav"><span class="btn btn--primary">Next</span></div>
  <h1 class="title" style="top:96px">What type of property would<br>you like to compare?</h1>
  <div class="type-tiles">
    <div class="tile tile--selected"><div class="tile__art" role="img" aria-label="Illustration of an apartment building"></div><div class="tile__label">Unit</div></div>
    <div class="tile"><div class="tile__art tile__art--house" role="img" aria-label="Illustration of a house"></div><div class="tile__label">House</div></div>
  </div>
  <footer class="footer">© 2019 Halvard Wealth. All Rights Reserved</footer>
</section>

<section class="screen screen--location">
  <div class="stepper">
    <div class="stepper__track"></div>
    <div class="stepper__progress" style="width:173px"></div>
    <div class="step step--done" style="left:116px"><span class="step__num">01</span><div class="step__dot"><svg width="10" height="10" viewBox="0 0 10 10"><path d="M2 5l2 2 4-4" fill="none" stroke="#0455a3" stroke-width="1.6"/></svg></div><span class="step__label">Property Type</span></div>
    <div class="step step--active" style="left:289px"><span class="step__num">02</span><div class="step__dot"></div><span class="step__label">Property Location</span></div>
    <div class="step" style="left:462px"><span class="step__num">03</span><div class="step__dot"></div><span class="step__label">Property Valuation</span></div>
    <div class="step" style="left:635px"><span class="step__num">04</span><div class="step__dot"></div><span class="step__label">Your Property Forecast</span></div>
    <div class="step" style="left:808px"><span class="step__num">05</span><div class="step__dot"></div><span class="step__label">Calculation</span></div>
  </div>
  <div class="nav"><span class="btn btn--ghost">Previous</span><span class="btn btn--primary">Next</span></div>
  <h1 class="title" style="top:100px">Where would this property be located?</h1>
  <div class="map" role="img" aria-label="Map of Australia with selectable states and a location pin"></div>
  <div class="slider-group" style="top:160px">
    <div class="slider-group__label">How much will the property cost? <span class="info">i</span></div>
    <div class="slider"><div class="slider__rail"></div><div class="slider__fill" style="width:90px"></div><div class="slider__knob" style="left:82px"></div></div>
    <span class="slider-group__value">$ 500,000</span>
  </div>
  <div class="slider-group" style="top:262px">
    <div class="slider-group__label">How much will you invest? <span class="info">i</span></div>
    <div class="slider"><div class="slider__rail"></div><div class="slider__fill" style="width:40px"></div><div class="slider__knob" style="left:32px"></div></div>
    <span class="slider-group__value">$ 100,000</span>
  </div>
  <footer class="footer">© 2019 Halvard Wealth. All Rights Reserved</footer>
</section>

<section class="screen screen--valuation">
  <div class="stepper">
    <div class="stepper__track"></div>
    <div class="stepper__progress" style="width:346px"></div>
    <div class="step step--done" style="left:116px"><span class="step__num">01</span><div class="step__dot"><svg width="10" height="10" viewBox="0 0 10 10"><path d="M2 5l2 2 4-4" fill="none" stroke="#0455a3" stroke-width="1.6"/></svg></div><span class="step__label">Property Type</span></div>
    <div class="step step--done" style="left:289px"><span class="step__num">02</span><div class="step__dot"><svg width="10" height="10" viewBox="0 0 10 10"><path d="M2 5l2 2 4-4" fill="none" stroke="#0455a3" stroke-width="1.6"/></svg></div><span class="step__label">Property Location</span></div>
    <div class="step step--active" style="left:462px"><span class="step__num">03</span><div class="step__dot"></div><span class="step__label">Property Valuation</span></div>
    <div class="step" style="left:635px"><span class="step__num">04</span><div class="step__dot"></div><span class="step__label">Your Property Forecast</span></div>
    <div class="step" style="left:808px"><span class="step__num">05</span><div class="step__dot"></div><span class="step__label">Calculation</span></div>
  </div>
  <div class="nav"><span class="btn btn--ghost">Previous</span><span class="btn btn--primary">Next</span></div>
  <h1 class="title" style="top:100px">How would you like to forecast the returns<br>from property?</h1>
  <div class="methods">
    <div class="method">
      <div class="method__icon"><div class="method__diamond"></div><div class="method__art" role="img" aria-label="Icon of a wallet with cash" style="background:linear-gradient(150deg,#e0a040,#8a4a1c)"></div></div>
      <div class="method__name">Relative Cost</div>
      <p class="method__desc">Use this to value property based on mortgage cost relative to rent paid</p>
    </div>
    <div class="method">
      <div class="method__icon"><div class="method__diamond"></div><div class="method__art" role="img" aria-label="Icon of a money bag" style="background:linear-gradient(150deg,#f4c84a,#c47a1a)"></div></div>
      <div class="method__name">Relative to Wages</div>
      <p class="method__desc">Use this to value property based on mortgage cost relative to wages</p>
    </div>
    <div class="method">
      <div class="method__icon"><div class="method__diamond"></div><div class="method__art" role="img" aria-label="Icon of a house with a rising chart" style="background:linear-gradient(150deg,#86cae7,#c0392b)"></div></div>
      <div class="method__name">Using Rental Yield</div>
      <p class="method__desc">Use this to value property based on its rental yield</p>
    </div>
  </div>
  <footer class="footer">© 2019 Halvard Wealth. All Rights Reserved</footer>
</section>

<section class="screen screen--forecast">
  <div class="stepper">
    <div class="stepper__track"></div>
    <div class="stepper__progress" style="width:519px"></div>
    <div class="step step--done" style="left:116px"><span class="step__num">01</span><div class="step__dot"><svg width="10" height="10" viewBox="0 0 10 10"><path d="M2 5l2 2 4-4" fill="none" stroke="#0455a3" stroke-width="1.6"/></svg></div><span class="step__label">Property Type</span></div>
    <div class="step step--done" style="left:289px"><span class="step__num">02</span><div class="step__dot"><svg width="10" height="10" viewBox="0 0 10 10"><path d="M2 5l2 2 4-4" fill="none" stroke="#0455a3" stroke-width="1.6"/></svg></div><span class="step__label">Property Location</span></div>
    <div class="step step--done" style="left:462px"><span class="step__num">03</span><div class="step__dot"><svg width="10" height="10" viewBox="0 0 10 10"><path d="M2 5l2 2 4-4" fill="none" stroke="#0455a3" stroke-width="1.6"/></svg></div><span class="step__label">Property Valuation</span></div>
    <div class="step step--active" style="left:635px"><span class="step__num">04</span><div class="step__dot"></div><span class="step__label">Your Property Forecast</span></div>
    <div class="step" style="left:808px"><span class="step__num">05</span><div class="step__dot"></div><span class="step__label">Calculation</span></div>
  </div>
  <div class="nav"><span class="btn btn--ghost">Previous</span><span class="btn btn--primary">Next</span></div>
  <h1 class="title forecast-title">Your Property price Forecast</h1>
  <div class="field" style="top:148px">Your base forecast for property price falls by<span class="field__input">Enter a percentage</span><span class="field__btn"><svg width="10" height="10" viewBox="0 0 10 10"><path d="M3 2l4 3-4 3" fill="none" stroke="#fff" stroke-width="1.6"/></svg></span></div>
  <div class="field" style="top:184px">You can see how this rate has changed in the past for Sydney houses<span class="field__input">Sydney House</span><span class="field__btn"><svg width="10" height="10" viewBox="0 0 10 10"><path d="M3 2l4 3-4 3" fill="none" stroke="#fff" stroke-width="1.6"/></svg></span></div>
  <svg class="chart" width="960" height="160" viewBox="0 0 960 160" role="img" aria-label="Line chart of forecast property price over time">
    <g stroke="#e6eaf0" stroke-width="1">
      <line x1="40" y1="30" x2="940" y2="30"/><line x1="40" y1="65" x2="940" y2="65"/><line x1="40" y1="100" x2="940" y2="100"/><line x1="40" y1="135" x2="940" y2="135"/>
    </g>
    <g font-family="Ubuntu, sans-serif" font-size="9" fill="#8a94a3">
      <text x="8" y="33">1.2</text><text x="8" y="68">0.8</text><text x="8" y="103">0.4</text><text x="8" y="138">0</text>
      <text x="60" y="152">2000</text><text x="240" y="152">2005</text><text x="420" y="152">2010</text><text x="600" y="152">2015</text><text x="780" y="152">2020</text>
    </g>
    <rect x="430" y="8" width="10" height="4" fill="#3176b5"/><text x="446" y="13" font-family="Ubuntu, sans-serif" font-size="9" fill="#556070">Forecast value</text>
    <rect x="530" y="8" width="10" height="4" fill="#86cae7"/><text x="546" y="13" font-family="Ubuntu, sans-serif" font-size="9" fill="#556070">Historic</text>
    <polyline fill="none" stroke="#3176b5" stroke-width="2" points="40,40 80,46 120,44 160,58 200,54 240,66 280,62 320,70 360,66 400,78 440,74 480,84 520,80 560,90 600,86 640,94 680,92 720,98 760,96 800,104 840,102 880,108 940,112"/>
  </svg>
  <p class="forecast-note">By default we assume the rate stays at whatever level it is. Move the slider to change the assumption.</p>
  <div class="slider forecast-slider"><div class="slider__rail"></div><div class="slider__fill" style="width:14px"></div><div class="slider__knob" style="left:6px"></div></div>
  <footer class="footer">© 2019 Halvard Wealth. All Rights Reserved</footer>
</section>

<section class="screen screen--calc">
  <div class="stepper">
    <div class="stepper__track"></div>
    <div class="stepper__progress" style="width:692px"></div>
    <div class="step step--done" style="left:116px"><span class="step__num">01</span><div class="step__dot"><svg width="10" height="10" viewBox="0 0 10 10"><path d="M2 5l2 2 4-4" fill="none" stroke="#0455a3" stroke-width="1.6"/></svg></div><span class="step__label">Property Type</span></div>
    <div class="step step--done" style="left:289px"><span class="step__num">02</span><div class="step__dot"><svg width="10" height="10" viewBox="0 0 10 10"><path d="M2 5l2 2 4-4" fill="none" stroke="#0455a3" stroke-width="1.6"/></svg></div><span class="step__label">Property Location</span></div>
    <div class="step step--done" style="left:462px"><span class="step__num">03</span><div class="step__dot"><svg width="10" height="10" viewBox="0 0 10 10"><path d="M2 5l2 2 4-4" fill="none" stroke="#0455a3" stroke-width="1.6"/></svg></div><span class="step__label">Property Valuation</span></div>
    <div class="step step--done" style="left:635px"><span class="step__num">04</span><div class="step__dot"><svg width="10" height="10" viewBox="0 0 10 10"><path d="M2 5l2 2 4-4" fill="none" stroke="#0455a3" stroke-width="1.6"/></svg></div><span class="step__label">Your Property Forecast</span></div>
    <div class="step step--active" style="left:808px"><span class="step__num">05</span><div class="step__dot"></div><span class="step__label">Calculation</span></div>
  </div>
  <div class="nav"><span class="btn btn--ghost">Previous</span><span class="btn btn--primary">Recalculate</span></div>
  <div class="results">
    <div class="results__cell results__cell--inputs">
      <div class="kv">Property Value<span class="kv__box">$ 500,000</span></div>
      <div class="kv">Deposit<span class="kv__box">$ 100,000</span></div>
      <div class="kv">Interest Rate<span class="kv__box">4.2 %</span></div>
      <div class="kv">Rental Income<span class="kv__box">$ 450 / week</span></div>
      <div class="kv">Holding Period<span class="kv__box">5 years</span></div>
    </div>
    <div class="results__cell">
      <svg width="100%" height="180" viewBox="0 0 390 180" preserveAspectRatio="none" role="img" aria-label="Line chart of projected returns">
        <g stroke="#33405a" stroke-width="1"><line x1="20" y1="40" x2="380" y2="40"/><line x1="20" y1="80" x2="380" y2="80"/><line x1="20" y1="120" x2="380" y2="120"/><line x1="20" y1="160" x2="380" y2="160"/></g>
        <polyline fill="none" stroke="#86cae7" stroke-width="2" points="20,130 50,120 80,124 110,108 140,112 170,96 200,100 230,86 260,90 290,74 320,78 350,62 380,58"/>
        <polyline fill="none" stroke="#3176b5" stroke-width="2" points="20,140 60,136 100,138 140,128 180,130 220,120 260,122 300,112 340,110 380,102"/>
      </svg>
    </div>
    <div class="results__cell">
      <svg width="100%" height="180" viewBox="0 0 390 180" preserveAspectRatio="none" role="img" aria-label="Column chart of yearly cash flow">
        <g stroke="#33405a" stroke-width="1"><line x1="10" y1="90" x2="380" y2="90"/></g>
        <g fill="#3176b5">
          <rect x="16" y="60" width="8" height="30"/><rect x="36" y="70" width="8" height="20"/><rect x="56" y="56" width="8" height="34"/><rect x="76" y="66" width="8" height="24"/><rect x="96" y="52" width="8" height="38"/><rect x="116" y="64" width="8" height="26"/><rect x="136" y="50" width="8" height="40"/><rect x="156" y="62" width="8" height="28"/><rect x="176" y="48" width="8" height="42"/><rect x="196" y="60" width="8" height="30"/><rect x="216" y="46" width="8" height="44"/>
        </g>
        <g fill="#86cae7">
          <rect x="26" y="90" width="8" height="22"/><rect x="46" y="90" width="8" height="30"/><rect x="66" y="90" width="8" height="20"/><rect x="86" y="90" width="8" height="28"/><rect x="106" y="90" width="8" height="18"/><rect x="126" y="90" width="8" height="26"/><rect x="146" y="90" width="8" height="16"/><rect x="166" y="90" width="8" height="24"/><rect x="186" y="90" width="8" height="14"/><rect x="206" y="90" width="8" height="22"/>
        </g>
      </svg>
      <div class="tooltip">After 5 years<br><b>Net return: $ 84,200</b><br>Total interest paid<br><b>$ 96,500</b></div>
    </div>
  </div>
  <p class="results-note">Note: These are indicative figures based on a simple range of assumptions. Halvard Wealth is not a financial planner; before making any investment decision, speak with a licensed adviser.</p>
  <footer class="footer">© 2019 Halvard Wealth. All Rights Reserved</footer>
</section>

</body>
</html>
```